Banner Ad Needed For Real Estate Lending Firm

We are taking out a banner ad on one of the most highly trafficked real estate websites in New York. The ad will be 970x250. Display format will be JPEG or animated GIF, but original art files will be required as well from the winning designer.

Granite Path Lending (or GPL) is one of the largest "hard money lenders" for real estate investors on the East Coast of the US. We lend for the following real estate investments: 1) Fix And Flip 2) New Construction 3) Cash Out Refinance. We close in 2-10 days. More information can be found on our website here: http://www.gpl7.example/

Our goal is to help small business owners, real estate investors, and commercial contractors quickly and efficiently finance their business activities. Our local hard money loan programs are tailored to your unique project needs. We fund fix and flip, new construction, and cash out refinance projects for non-owner occupied properties.

Target Market(s)

Real Estate Agents, Real Estate Investors, Mortgage Brokers, Other Real Estate Professionals

Industry/Entity Type

Real Estate

Font styles to use
Sans Serif

Requirements
Must have
• Must incorporate the fact that we close deals very fast (2 - 10 days), finance the following these 2 main types of investments (Fix and Flip, New Construction), and mention that Brokers can make up to 2.5 Points.
• See attached style guide for basic colors and fonts.
Nice to have
• Animated GIF might be a great feature!

```html
<!DOCTYPE html>
<html lang="en">
<head>
<meta charset="utf-8">
<title>Granite Path Lending – Banner Set</title>
<link rel="stylesheet" href="https://fonts.googleapis.com/css2?family=Montserrat:ital,wght@0,400;0,500;0,600;0,700;1,400;1,600&family=Roboto+Slab:wght@300;400&display=swap">
<style>
  :root {
    --bg-orange: #fdaf2e;
    --white: #ffffff;
    --navy: #1f4e5f;
    --green: #2e7a5d;
    --mark-green: #4a7c6a;
    --teal: #0b5666;
    --teal-box: #176a79;
    --ice: #a9d8de;
    --badge: #5e9ea6;
    --badge-num: #f6c66a;
    --cta: #f5a31a;
  }
  * { margin: 0; padding: 0; box-sizing: border-box; }
  html, body { width: 1200px; height: 1043px; overflow: hidden; background: var(--bg-orange); }
  .stage {
    position: relative; width: 1150px; height: 1000px;
    transform: scale(1.04348); transform-origin: 0 0;
    font-family: "Montserrat", sans-serif;
  }
  .banner { position: absolute; left: 88px; width: 970px; height: 250px; display: flex; }
  .banner--one { top: 83px; }
  .banner--two { top: 377px; }
  .banner--three { top: 670px; }

  .badge {
    position: absolute; left: 283px; top: -28px; width: 56px; height: 56px; border-radius: 50%;
    background: var(--badge); color: var(--badge-num); font-size: 30px; font-weight: 600;
    display: flex; align-items: center; justify-content: center; z-index: 2;
  }

  .brand { width: 349px; background: var(--white); position: relative; }
  .brand__square { position: absolute; left: 26px; top: 36px; width: 70px; height: 70px; background: var(--mark-green); }
  .brand__name {
    position: absolute; left: 120px; top: 28px; color: var(--navy);
    font-size: 22px; font-weight: 700; line-height: 31px;
  }
  .brand__rule { position: absolute; left: 136px; top: 141px; width: 74px; height: 2px; background: var(--navy); }
  .brand__phone {
    position: absolute; left: 0; width: 349px; top: 158px; text-align: center;
    color: var(--navy); font-size: 33px; font-weight: 500; letter-spacing: 1px;
  }
  .brand__email {
    position: absolute; left: 0; width: 349px; top: 205px; text-align: center;
    color: var(--green); font-size: 20px; font-weight: 600; letter-spacing: 1px;
  }

  .pitch { width: 347px; background: var(--teal); position: relative; overflow: hidden; }
  .pitch__headline {
    position: absolute; left: 0; top: 14px; width: 347px; text-align: center;
    color: var(--white); font-size: 35px; font-weight: 400; line-height: 46px;
  }
  .feature {
    position: absolute; left: 19px; top: 157px; width: 309px; height: 93px;
    background: var(--teal-box); border-radius: 8px 8px 0 0; color: var(--ice);
  }
  .feature__icon { position: absolute; left: 14px; top: 16px; width: 50px; height: 56px; }
  .feature__title {
    position: absolute; left: 70px; top: 5px; font-family: "Roboto Slab", serif;
    font-weight: 300; font-size: 23px; white-space: nowrap;
  }
  .feature__text {
    position: absolute; left: 70px; top: 39px; width: 236px;
    font-size: 13px; font-style: italic; line-height: 17px;
  }
  .feature__text strong { font-weight: 600; text-decoration: underline; }

  .offer { width: 274px; position: relative; overflow: hidden; }
  .offer__photo { position: absolute; inset: 0; }
  .offer__photo--renovation { background: linear-gradient(135deg, #8a6a4c 0%, #5b4637 45%, #a98a6c 75%, #6e5644 100%); }
  .offer__photo--construction { background: linear-gradient(160deg, #c9d3dc 0%, #a38a6c 45%, #7b6551 75%, #4f4a46 100%); }
  .offer__title {
    position: absolute; left: 0; width: 274px; top: 74px; text-align: center;
    color: var(--white); font-size: 26px; line-height: 35px; font-weight: 400;
  }
  .offer__cta {
    position: absolute; left: 142px; top: 182px; width: 127px; height: 50px;
    background: var(--cta); border: 1px solid var(--white);
    color: var(--white); font-weight: 700; font-size: 15px; line-height: 18px;
    display: flex; align-items: center; justify-content: center; text-align: center;
  }
  .offer__note {
    position: absolute; right: 5px; top: 235px; color: var(--white);
    font-size: 10.5px; font-weight: 500; white-space: nowrap;
  }
</style>
</head>
<body>
<div class="stage">

  <section class="banner banner--one">
    <div class="badge">1</div>
    <div class="brand">
      <div class="brand__square"></div>
      <div class="brand__name">GRANITE<br>PATH<br>LENDING LLC</div>
      <div class="brand__rule"></div>
      <div class="brand__phone">555.014.2290</div>
      <div class="brand__email">info@gpl7.example</div>
    </div>
    <div class="pitch">
      <h2 class="pitch__headline">LOOKING FOR<br>A HARD MONEY<br>LOANS?</h2>
      <div class="feature">
        <svg class="feature__icon" viewBox="0 0 52 58" fill="none" stroke="currentColor" stroke-width="2">
          <rect x="21" y="2" width="10" height="5"/><line x1="26" y1="7" x2="26" y2="12"/>
          <circle cx="26" cy="34" r="22"/><circle cx="26" cy="34" r="17"/>
          <line x1="26" y1="34" x2="26" y2="22"/><line x1="26" y1="34" x2="33" y2="38"/>
          <line x1="43" y1="15" x2="47" y2="11"/>
        </svg>
        <div class="feature__title">Fast Processing</div>
        <p class="feature__text">We’ve closed loans in <strong>48 hours</strong>, and average just 10 days.</p>
      </div>
    </div>
    <div class="offer">
      <div class="offer__photo offer__photo--renovation" role="img" aria-label="Photo of a worker fitting kitchen cabinets"></div>
      <h3 class="offer__title">Fix and Flip Hard<br>Money Loans</h3>
      <div class="offer__cta">PREQUALIFY<br>TODAY</div>
      <p class="offer__note">Brokers can make up to 2.5 Points</p>
    </div>
  </section>

  <section class="banner banner--two">
    <div class="badge">2</div>
    <div class="brand">
      <div class="brand__square"></div>
      <div class="brand__name">GRANITE<br>PATH<br>LENDING LLC</div>
      <div class="brand__rule"></div>
      <div class="brand__phone">555.014.2290</div>
      <div class="brand__email">info@gpl7.example</div>
    </div>
    <div class="pitch">
      <h2 class="pitch__headline">LOOKING FOR<br>A HARD MONEY<br>LOANS?</h2>
      <div class="feature">
        <svg class="feature__icon" viewBox="0 0 52 58" fill="none" stroke="currentColor" stroke-width="2">
          <rect x="12" y="14" width="30" height="40"/><rect x="8" y="10" width="30" height="40" fill="#176a79"/>
          <rect x="4" y="6" width="30" height="40" fill="#176a79"/>
          <line x1="12" y1="22" x2="26" y2="22"/><line x1="12" y1="28" x2="26" y2="28"/><line x1="15" y1="34" x2="23" y2="34"/>
          <path d="M9 2v12a3 3 0 0 0 6 0V5"/>
        </svg>
        <div class="feature__title">Flexible Underwriting</div>
        <p class="feature__text">GPL has <strong>no minimum credit score</strong> requirements.</p>
      </div>
    </div>
    <div class="offer">
      <div class="offer__photo offer__photo--renovation" role="img" aria-label="Photo of a worker fitting kitchen cabinets"></div>
      <h3 class="offer__title">Fix and Flip Hard<br>Money Loans</h3>
      <div class="offer__cta">PREQUALIFY<br>TODAY</div>
      <p class="offer__note">Brokers can make up to 2.5 Points</p>
    </div>
  </section>

  <section class="banner banner--three">
    <div class="badge">3</div>
    <div class="brand">
      <div class="brand__square"></div>
      <div class="brand__name">GRANITE<br>PATH<br>LENDING LLC</div>
      <div class="brand__rule"></div>
      <div class="brand__phone">555.014.2290</div>
      <div class="brand__email">info@gpl7.example</div>
    </div>
    <div class="pitch">
      <h2 class="pitch__headline">LOOKING FOR<br>A HARD MONEY<br>LOANS?</h2>
      <div class="feature">
        <svg class="feature__icon" viewBox="0 0 52 58" fill="none" stroke="currentColor" stroke-width="2">
          <path d="M4 30 L24 10 L40 10 L40 26 L20 46 Z"/><circle cx="33" cy="17" r="3"/>
          <circle cx="38" cy="42" r="10" fill="#176a79"/><path d="M33 42 l4 4 l7 -8"/>
        </svg>
        <div class="feature__title">Competitive Rates</div>
        <p class="feature__text">Fix and flip interest rates of <strong>9%-12%</strong> &amp; new construction <strong>10%-12%</strong> with <strong>2-3 points</strong>.</p>
      </div>
    </div>
    <div class="offer">
      <div class="offer__photo offer__photo--construction" role="img" aria-label="Photo of a builder in a hard hat reading plans in front of a new house"></div>
      <h3 class="offer__title">New Construction<br>Hard Money Loans</h3>
      <div class="offer__cta">PREQUALIFY<br>TODAY</div>
      <p class="offer__note">Brokers can make up to 2.5 Points</p>
    </div>
  </section>

</div>
</body>
</html>
```